we need a design for Water Bottle Lable Wrap
The product is called Calmora Springs is a restructured water. its a very healthy and rejuvenating water
we were looking at using as a tag ling Restore, Recover, Rejuvenate.

```html
<!DOCTYPE html>
<html lang="en">
<head>
<meta charset="utf-8">
<title>Calmora Springs – Bottle Label Wrap</title>
<link rel="stylesheet" href="https://fonts.googleapis.com/css2?family=Oswald:wght@600;700&family=Sansita:ital,wght@1,700&display=swap">
<style>
  :root {
    --canvas-bg: #eef4f8;
    --label-top: #a9d3ee;
    --label-bottom: #8ec6ea;
    --brand-blue: #1a5fe0;
    --aqua: #1faee8;
    --mark-blue: #2a7ff0;
  }
  html, body {
    margin: 0;
    width: 1200px;
    height: 1200px;
    overflow: hidden;
    background: var(--canvas-bg);
  }
  .canvas {
    width: 1200px;
    height: 1200px;
    display: flex;
    align-items: center;
    justify-content: center;
  }
  .label-wrap {
    width: 560px;
    height: 1080px;
    border-radius: 18px;
    background: linear-gradient(180deg, var(--label-top), var(--label-bottom));
    display: flex;
    flex-direction: column;
    align-items: center;
    box-sizing: border-box;
    padding-top: 190px;
  }
  .brand-mark {
    width: 300px;
    height: 300px;
    border-radius: 50%;
    background: var(--mark-blue);
    opacity: 0.85;
  }
  .brand-name {
    margin: 60px 0 0;
    font-family: "Oswald", sans-serif;
    font-weight: 700;
    font-size: 84px;
    letter-spacing: 1px;
    line-height: 1;
    color: var(--brand-blue);
  }
  .tagline {
    margin: 36px 0 0;
    padding: 0;
    list-style: none;
    text-align: center;
    font-family: "Sansita", sans-serif;
    font-style: italic;
    font-weight: 700;
    font-size: 38px;
    line-height: 1.22;
    color: var(--aqua);
  }
  .product-type {
    margin: 78px 0 0;
    font-family: "Oswald", sans-serif;
    font-weight: 600;
    font-size: 34px;
    letter-spacing: 0.5px;
    color: var(--brand-blue);
  }
  .volume {
    margin: 16px 0 0;
    font-family: "Oswald", sans-serif;
    font-weight: 600;
    font-size: 30px;
    color: var(--brand-blue);
  }
</style>
</head>
<body>
  <main class="canvas">
    <section class="label-wrap">
      <div class="brand-mark" aria-hidden="true"></div>
      <h1 class="brand-name">CALMORA</h1>
      <ul class="tagline">
        <li>Restore</li>
        <li>Recover</li>
        <li>Rejuvenate</li>
      </ul>
      <p class="product-type">RESTRUCTURED WATER</p>
      <p class="volume">12oz</p>
    </section>
  </main>
</body>
</html>
```